PLUME Residence One-Page Inserts

We need TWO one-page insert for a transplant display stand (6"x8"). We have a few furnished apartments and we need to inform our guests about the services available:

Insert #1: Delivery and Pickup Services in the neighborhood (Laundry, Groceries, Restaurants).
Insert #1 Text: "Heading: Pick and Delivery Services in your neighborhood:" Text below it: "1) Laundry Pickup - Call: +9714-382-7160. 2) Groceries Delivery - Call: +9714-382-7160, 3) Restaurants Delivery - Call: +9714-382-7160"

Insert #2: We also need another one-page insert to encourage the guests to enjoy the candles and to make the apartment have a homier feeling.
Insert #2 Text: "Heading: Feel at home. Text below it: "Dim the lights, light up a candle, play nice music, have a relaxing stay."

Target Market(s)

Staybrook Users. Apartment Guests. Tourist. Age Group 20 to 60 years old.

Industry/Entity Type

Hotel

Requirements
Must have
• - The Company logo of PLUME Residence must be displayed on the upper corner. (Logo attached). The logo should be a single color either white or black (Not red and black or red and white)
• For Insert # 1: Laundry, Groceries, and Breakfast Resturaunts images or icons. The images/icons must be unified and look like from the same family of images/icons.
• For Insert # 2: A romantic candle(s) dinner pictures.
Nice to have
• Not too many colors
• Not too busy
• Simple
• Eye Catchy
Should not have
• Lots of colors
• Too many images
• Too Busy

```html
<!DOCTYPE html>
<html lang="en">
<head>
<meta charset="utf-8">
<title>PLUME Residence – Guest Inserts</title>
<link href="https://fonts.googleapis.com/css2?family=Open+Sans:wght@400;600&display=swap" rel="stylesheet">
<style>
  :root {
    --backdrop: #d6d6d6;
    --brand-red: #b91f27;
    --red-deep: #a11b22;
    --red-soft: #c9453f;
    --ink-dark: #1b1b1b;
    --white: #ffffff;
    --pill: #e9e9e9;
    --pill-text-red: #b91f27;
    --pill-text-dark: #222222;
  }
  * { box-sizing: border-box; margin: 0; padding: 0; }
  html, body { width: 845px; height: 1200px; overflow: hidden; }
  body {
    background: var(--backdrop);
    font-family: "Open Sans", Arial, sans-serif;
    color: var(--white);
    position: relative;
  }
  .insert {
    position: absolute;
    left: 102px;
    width: 630px;
    height: 470px;
    overflow: hidden;
  }
  .insert--services { top: 104px; background: var(--brand-red); }
  .insert--home {
    top: 627px;
    height: 471px;
    background: radial-gradient(ellipse 55% 60% at 50% 50%, #4a4a4a 0%, #2a2a2a 55%, var(--ink-dark) 100%);
  }
  .wordmark {
    position: absolute;
    left: 0; right: 0;
    text-align: center;
    font-weight: 400;
    font-size: 60px;
    line-height: 1;
    letter-spacing: 2px;
    color: var(--white);
  }
  .insert--services .wordmark { top: 72px; }
  .insert--home .wordmark { top: 120px; }
  .headline {
    position: absolute;
    left: 0; right: 0;
    top: 170px;
    text-align: center;
    font-weight: 600;
    font-size: 21px;
    line-height: 1.2;
    text-transform: uppercase;
  }
  .skyline {
    position: absolute;
    left: 0; right: 0; bottom: 0;
    height: 78px;
    background: linear-gradient(to top, var(--red-deep) 55%, rgba(161,27,34,0.35));
  }
  .service {
    position: absolute;
    top: 215px;
    width: 190px;
    margin-left: -95px;
    text-align: center;
  }
  .service__badge {
    width: 110px;
    height: 110px;
    margin: 0 auto;
    display: block;
  }
  .service__name {
    margin-top: 14px;
    font-weight: 600;
    font-size: 15px;
    text-transform: uppercase;
    white-space: nowrap;
  }
  .service__phone {
    margin-top: 6px;
    font-size: 13px;
    display: flex;
    align-items: center;
    justify-content: center;
    gap: 8px;
  }
  .service__phone svg { width: 14px; height: 14px; }
  .web-pill {
    position: absolute;
    left: 196px;
    width: 238px;
    height: 26px;
    border-radius: 8px;
    background: var(--pill);
    text-align: center;
    font-size: 14px;
    line-height: 26px;
    z-index: 2;
  }
  .insert--services .web-pill { top: 411px; color: var(--pill-text-red); }
  .insert--home .web-pill { top: 302px; color: var(--pill-text-dark); }
  .home-title {
    position: absolute;
    left: 0; right: 0;
    top: 220px;
    text-align: center;
    font-weight: 600;
    font-size: 21px;
    text-transform: uppercase;
  }
  .home-text {
    position: absolute;
    left: 0; right: 0;
    top: 254px;
    text-align: center;
    font-size: 14px;
  }
  .candle-photo {
    position: absolute;
    left: 18px;
    top: 338px;
    width: 214px;
    height: 122px;
    border-radius: 40% 40% 48% 48% / 35% 35% 30% 30%;
    background: radial-gradient(ellipse at 50% 40%, #f3e7c6 0%, #cfc2a0 40%, #8d877b 70%, rgba(40,40,40,0) 100%);
  }
</style>
</head>
<body>

<section class="insert insert--services">
  <div class="skyline" role="img" aria-label="City skyline silhouette in deep red"></div>
  <div class="wordmark">PLUME</div>
  <h1 class="headline">Pick and delivery services in your neighborhood</h1>

  <div class="service" style="left:130px">
    <svg class="service__badge" viewBox="0 0 110 110">
      <circle cx="55" cy="55" r="52" fill="var(--brand-red)" stroke="var(--white)" stroke-width="5"/>
      <path d="M8 50 A47 47 0 0 1 102 50 A60 30 0 0 0 8 50Z" fill="var(--red-soft)"/>
      <path d="M55 22 q5 0 5 5 q0 4 -5 6 v4" fill="none" stroke="#fff" stroke-width="2.5"/>
      <path d="M29 52 L55 37 L81 52" fill="none" stroke="#fff" stroke-width="4" stroke-linejoin="round"/>
      <rect x="38" y="50" width="34" height="37" fill="#fff"/>
    </svg>
    <div class="service__name">Laundry Pickup</div>
    <div class="service__phone">
      <svg viewBox="0 0 14 14"><circle cx="7" cy="7" r="6" fill="none" stroke="#fff" stroke-width="1.2"/><path d="M4.6 4 l1.3-.3 .7 1.6 -.8.6 q.6 1.4 1.8 1.9 l.6-.8 1.6.7 -.3 1.3 q-3.5 .2-4.9-5z" fill="#fff"/></svg>
      +9714-382-7160
    </div>
  </div>

  <div class="service" style="left:315px">
    <svg class="service__badge" viewBox="0 0 110 110">
      <circle cx="55" cy="55" r="52" fill="var(--brand-red)" stroke="var(--white)" stroke-width="5"/>
      <path d="M8 50 A47 47 0 0 1 102 50 A60 30 0 0 0 8 50Z" fill="var(--red-soft)"/>
      <path d="M42 55 L53 32 M68 55 L57 32" stroke="#fff" stroke-width="4" stroke-linecap="round"/>
      <path d="M26 55 H84 L78 84 H32 Z" fill="none" stroke="#fff" stroke-width="5" stroke-linejoin="round"/>
      <path d="M43 64 V77 M51 64 V77 M59 64 V77 M67 64 V77" stroke="#fff" stroke-width="4"/>
    </svg>
    <div class="service__name">Groceries Delivery</div>
    <div class="service__phone">
      <svg viewBox="0 0 14 14"><circle cx="7" cy="7" r="6" fill="none" stroke="#fff" stroke-width="1.2"/><path d="M4.6 4 l1.3-.3 .7 1.6 -.8.6 q.6 1.4 1.8 1.9 l.6-.8 1.6.7 -.3 1.3 q-3.5 .2-4.9-5z" fill="#fff"/></svg>
      +9714-382-7160
    </div>
  </div>

  <div class="service" style="left:502px">
    <svg class="service__badge" viewBox="0 0 110 110">
      <circle cx="55" cy="55" r="52" fill="var(--brand-red)" stroke="var(--white)" stroke-width="5"/>
      <path d="M8 50 A47 47 0 0 1 102 50 A60 30 0 0 0 8 50Z" fill="var(--red-soft)"/>
      <circle cx="55" cy="34" r="5" fill="#fff"/>
      <path d="M30 70 A25 25 0 0 1 80 70 Z" fill="#fff"/>
      <rect x="24" y="73" width="62" height="5" rx="1" fill="#fff"/>
    </svg>
    <div class="service__name">Restaurants Delivery</div>
    <div class="service__phone">
      <svg viewBox="0 0 14 14"><circle cx="7" cy="7" r="6" fill="none" stroke="#fff" stroke-width="1.2"/><path d="M4.6 4 l1.3-.3 .7 1.6 -.8.6 q.6 1.4 1.8 1.9 l.6-.8 1.6.7 -.3 1.3 q-3.5 .2-4.9-5z" fill="#fff"/></svg>
      +9714-382-7160
    </div>
  </div>

  <div class="web-pill">www.plumeresidence.com</div>
</section>

<section class="insert insert--home">
  <div class="wordmark">PLUME</div>
  <h2 class="home-title">Feel at home</h2>
  <p class="home-text">Dim the lights, light up a candle, play nice music, have a relaxing stay.</p>
  <div class="web-pill">www.plumeresidence.com</div>
  <div class="candle-photo" role="img" aria-label="Photo of lit white pillar candles on a plate of smooth pebbles"></div>
</section>

</body>
</html>
```